Drifting Ages Chronicle - Book Cover Design

I need a cover (front, spine, back) designed for the second edition of the historical book - Drifting Ages Chronicle. This book was created to be a more engaging supplementary resource to the dry texts of most middle and high school social studies classrooms. Although comprehensive and exhaustively researched, the book at times uses humor and irony to engage the reader. The cover should reflect this tone.

Book Title: Drifting Ages Chronicle
Subtitle: The Tales, Traditions and Turning Points of World History and the Regional Challenges of Today
Author: Noel Wickstrom
Updates

Project Deadline Extended
Reason: As multiple designers are working on adjustments and I am looking for new, creative ideas, I am extending the deadline five days. Thank you.

Project Deadline Extended
Reason: Artists are still making alterations to suggestions made and I also want to give designers a chance to submit new ideas.

Target Market(s)

Middle School and High School Teachers

Font styles to use
Serif

Colors
ec1f27
ffffff
000000

Requirements
Must have
• 1) See attachment for text for front cover, spine, back cover
• 2) Central, engaging image
Nice to have
• A subtle hint of humor, light tone
• Potentially upside down globe spinning
• Prefer black, red, white color scheme
Should not have
• Cartoonish text, images

```html
<!DOCTYPE html>
<html lang="en">
<head>
<meta charset="utf-8">
<title>Drifting Ages Chronicle – Cover</title>
<link rel="stylesheet" href="https://fonts.googleapis.com/css2?family=Cinzel:wght@400;500&family=EB+Garamond:wght@400&family=Open+Sans:wdth,wght@75..100,400..700&family=Tinos:wght@400;700&display=swap">
<style>
  :root {
    --red: #ec1f27;
    --black: #000000;
    --white: #ffffff;
    --paper: #f4f3ef;
    --ink-panel: #3a3a3a;
    --spine: #3b3b3b;
    --stage: #e9e9e9;
  }
  * { box-sizing: border-box; margin: 0; padding: 0; }
  html, body { width: 1200px; height: 1200px; overflow: hidden; }
  body { background: var(--stage); position: relative; }

  .cover-wrap {
    position: absolute; left: 32px; top: 210px;
    width: 1136px; height: 780px;
    display: flex;
    box-shadow: 0 18px 40px rgba(0,0,0,.18);
  }

  /* Back cover */
  .back-cover {
    width: 540px; height: 100%;
    background: var(--paper);
    position: relative;
  }
  .note {
    position: absolute; left: 40px; top: 58px;
    width: 460px; height: 590px;
    background: var(--white);
    box-shadow: 0 10px 22px rgba(0,0,0,.22);
    border-bottom-right-radius: 40px 18px;
  }
  .note-panel {
    background: var(--ink-panel);
    color: var(--white);
    padding: 46px 20px 18px;
    font-family: "Open Sans", sans-serif;
    font-stretch: 80%;
  }
  .note-heading {
    font-size: 22px; font-weight: 700; font-stretch: 90%;
    text-align: center; margin-bottom: 10px;
  }
  .note-body {
    font-size: 13.6px; line-height: 1.32; text-align: justify;
    margin-bottom: 8px;
  }
  .note-body:last-child { margin-bottom: 0; }
  .note-quote {
    font-family: "Open Sans", sans-serif; font-stretch: 85%;
    font-size: 14px; line-height: 1.3; font-weight: 600;
    color: var(--black); text-align: center;
    padding: 16px 28px 0;
  }
  .note-quote .attribution { font-weight: 700; }
  .back-pin { position: absolute; left: 212px; top: -22px; }
  .code-box {
    position: absolute; right: 40px; bottom: 48px;
    width: 190px; height: 110px;
    border: 1px solid #9a9a9a; background: var(--white);
  }

  /* Spine */
  .spine {
    width: 56px; height: 100%;
    background: var(--spine);
    position: relative;
  }
  .spine-title {
    position: absolute; left: 50%; top: 40px;
    transform: translateX(-50%);
    writing-mode: vertical-rl;
    font-family: "Tinos", serif; font-size: 27px; letter-spacing: 2px;
    color: var(--white); white-space: nowrap;
  }
  .spine-author {
    position: absolute; left: 50%; bottom: 40px;
    transform: translateX(-50%);
    writing-mode: vertical-rl;
    font-family: "Cinzel", serif; font-size: 12px; letter-spacing: 1px;
    color: var(--red); white-space: nowrap;
  }

  /* Front cover */
  .front-cover {
    width: 540px; height: 100%;
    background: var(--paper);
    position: relative;
    text-align: center;
  }
  .author {
    position: absolute; left: 0; right: 0; top: 62px;
    font-family: "Cinzel", serif; font-weight: 400;
    font-size: 40px; color: var(--red); letter-spacing: 1px;
  }
  .globe-pin { position: absolute; left: 248px; top: 132px; z-index: 2; }
  .globe {
    position: absolute; left: 150px; top: 180px;
    width: 240px; height: 240px; border-radius: 50%;
    background: radial-gradient(circle at 40% 40%, #ffffff 0%, #d8d8d8 40%, #2f2f2f 75%);
    box-shadow: 0 6px 14px rgba(0,0,0,.2);
  }
  .title-block {
    position: absolute; left: 0; right: 0; top: 440px;
    transform: rotate(-7deg);
  }
  .title {
    font-family: "Tinos", serif; font-weight: 700;
    color: var(--red); line-height: .86; letter-spacing: -1px;
  }
  .title span { display: block; }
  .title .line-1 { font-size: 86px; }
  .title .line-2 { font-size: 104px; }
  .title .line-3 { font-size: 74px; }
  .subtitle {
    margin-top: 16px;
    font-family: "EB Garamond", serif; font-size: 24px; line-height: 1.12;
    color: var(--black);
  }
</style>
</head>
<body>
  <div class="cover-wrap">

    <section class="back-cover">
      <div class="note">
        <svg class="back-pin" width="36" height="56" viewBox="0 0 36 56" aria-hidden="true">
          <line x1="18" y1="30" x2="14" y2="54" stroke="#777" stroke-width="2"/>
          <ellipse cx="18" cy="30" rx="15" ry="5" fill="#c4161d"/>
          <rect x="12" y="10" width="12" height="20" fill="var(--red)"/>
          <ellipse cx="18" cy="10" rx="11" ry="5" fill="#f04a50"/>
        </svg>
        <div class="note-panel">
          <p class="note-heading">Do you know how we got to here?</p>
          <p class="note-body">Well, if you’re like 97.4% of the people walking the planet, you haven’t got a clue. Sure, you might know a bit about a couple rivers in Mesopotamia, how Teodric wandered around Athens asking questions or how Brother Anselm Hale got ticked off one day and nailed a really long essay to the door of a church. But to be honest (and don’t be embarrassed), you’ve got some gaps.</p>
          <p class="note-body">Be dense no more. In Drifting Ages Chronicle, Noel Wickstrom once again takes you through all the major tales, traditions and turning points of world history - not just European history, but WORLD history. You’ll figure out real quick that the West might have had some crowning moments, but for the whole of human history, it’s been the Persians, the Indians, the Chinese, the Muslims or some horse peoples from the steppe that have truly turned us into the clever little creatures we are today. And while most world history books fade off once the Cold War comes to a close, this sometimes sardonic tome just gets going. Updated to include contemporary debates over topics such as Brexit, the rise of ISIS, claims to the South China Sea, the mounting refugee crisis and the controversial presidency of Garrett Voss, this second edition finishes with a distinctively comprehensive look at the 21st century challenges facing nine major regions of today’s world - Africa, Latin America, Japan, China, the Middle East, India, Russia, Europe and the United States.</p>
        </div>
        <p class="note-quote">“ Noel Wickstrom expertly understands what his audience wants to know, what they need to know. A page-turning account of our proudest achievements and our most colossal bumblings. It’s world history for the rest of us. ” - <span class="attribution">Idris Kalem</span></p>
      </div>
      <div class="code-box"></div>
    </section>

    <section class="spine">
      <p class="spine-title">DRIFTING AGES CHRONICLE</p>
      <p class="spine-author">NOEL WICKSTROM</p>
    </section>

    <section class="front-cover">
      <p class="author">Noel Wickstrom</p>
      <svg class="globe-pin" width="44" height="62" viewBox="0 0 44 62" aria-hidden="true">
        <line x1="20" y1="34" x2="18" y2="60" stroke="#777" stroke-width="2"/>
        <ellipse cx="22" cy="34" rx="17" ry="6" fill="#c4161d"/>
        <rect x="15" y="12" width="14" height="22" fill="var(--red)"/>
        <ellipse cx="22" cy="12" rx="13" ry="6" fill="#f04a50"/>
      </svg>
      <div class="globe" role="img" aria-label="Black and white upside-down globe pinned at its top by a red pushpin"></div>
      <div class="title-block">
        <h1 class="title">
          <span class="line-1">DRIFTING</span>
          <span class="line-2">AGES</span>
          <span class="line-3">CHRONICLE</span>
        </h1>
        <p class="subtitle">The Tales, Traditions and Turning Points<br>of World History<br>and the Regional Challenges of Today</p>
      </div>
    </section>

  </div>
</body>
</html>
```